Fun and Professional Food Packaging

We need a packaging design (front and back) for raw vegan cookie snacks. Our company is called Sunny Grove Bites and the nut cookies are a representation of our lifestyle: healthy, energetic, Eco-friendly, multi-purpose, strong.

We definitely want to have a clear window or strip on the front of the packing, so please include that space in the design.
Updates

Project Deadline Extended
Reason: Please extend the deadline, so I could get a few more designs and think about it. Thank you!

Target Market(s)

Age group: adults
Gender: both
This is a specialty product (raw and vegan) so it is targeted to the health conscious consumer, but is not limited to this audience and ideally will target all.

Industry/Entity Type

Health Product

Font styles to use
Serif
Sans Serif

Requirements
Must have
• This products comes in: original, chocolate, cranberry, and pineapple flavors. So we are looking to have 1 universal design that can be customization by simply changing the color and a bit the text to indicate the flavor.
• Must have the labels: Vegan, raw, organic, non-gmo, glutern-free, kosher, paleo, cruelty-free.

```html
<!DOCTYPE html>
<html lang="en">
<head>
<meta charset="utf-8">
<title>Sunny Grove Bites – Nut Cookies Cranberry</title>
<link href="https://fonts.googleapis.com/css2?family=Montserrat:wght@700&family=Oswald:wght@500;600&family=Passion+One:wght@400&display=swap" rel="stylesheet">
<style>
  :root {
    --flavor-red: #e03a4b;
    --flavor-red-dark: #b82636;
    --ink: #4a4a4a;
    --paper: #f1f0ee;
    --pattern-tone: #e2e1df;
    --white: #ffffff;
  }
  * { margin: 0; padding: 0; box-sizing: border-box; }
  html, body { width: 836px; height: 1200px; overflow: hidden; background: var(--paper); }
  .pack {
    position: relative;
    width: 836px;
    height: 1200px;
    background: var(--paper);
    overflow: hidden;
  }
  .word-pattern {
    position: absolute;
    left: 0; top: 120px;
    width: 836px; height: 920px;
    background: linear-gradient(180deg, var(--pattern-tone), #ebeae8 50%, var(--pattern-tone));
  }
  .top-band { position: absolute; left: 0; top: 0; width: 836px; height: 150px; }
  .window {
    position: absolute;
    left: 148px; top: 441px;
    width: 532px; height: 532px;
    border-radius: 50%;
    clip-path: inset(262px 0 0 0);
    background: radial-gradient(circle at 50% 62%, #efe6d2 0%, #e2d2ad 55%, #c9a86a 100%);
  }
  .brand {
    position: absolute;
    top: 186px; left: 0; width: 100%;
    text-align: center;
    font-family: "Montserrat", sans-serif;
    font-weight: 700;
    font-size: 40px;
    color: var(--flavor-red);
  }
  .subtitle {
    position: absolute;
    top: 262px; left: 0; width: 100%;
    display: flex; justify-content: center; align-items: center; gap: 14px;
    font-family: "Oswald", sans-serif;
    font-weight: 600;
    font-size: 34px;
    color: var(--ink);
    letter-spacing: 0.5px;
  }
  .subtitle::before, .subtitle::after {
    content: ""; width: 58px; height: 4px; background: var(--flavor-red);
  }
  .product-name {
    position: absolute;
    left: 0; width: 100%;
    text-align: center;
    font-family: "Passion One", sans-serif;
    color: var(--ink);
    line-height: 1;
  }
  .product-name.line-1 { top: 314px; font-size: 166px; letter-spacing: 4px; }
  .product-name.line-2 { top: 470px; font-size: 140px; letter-spacing: 2px; }
  .flavor-banner { position: absolute; left: 130px; top: 640px; width: 576px; height: 84px; }
  .flavor-name {
    position: absolute;
    left: 0; top: 648px; width: 100%;
    text-align: center;
    font-family: "Montserrat", sans-serif;
    font-weight: 700;
    font-size: 46px;
    color: var(--white);
  }
  .net-weight {
    position: absolute;
    right: 92px; top: 996px;
    font-family: "Oswald", sans-serif;
    font-weight: 500;
    font-size: 27px;
    color: var(--ink);
  }
  .claims-band {
    position: absolute;
    left: 0; top: 1040px;
    width: 836px; height: 160px;
    background: var(--flavor-red);
    display: flex; justify-content: space-evenly; align-items: flex-start;
    padding: 26px 10px 0;
  }
  .claim { display: flex; flex-direction: column; align-items: center; gap: 12px; width: 90px; }
  .claim-badge {
    width: 54px; height: 54px;
    border: 3px solid var(--ink);
    border-radius: 50%;
  }
  .claim-label {
    font-family: "Oswald", sans-serif;
    font-weight: 500;
    font-size: 18px;
    color: var(--ink);
    white-space: nowrap;
  }
</style>
</head>
<body>
<main class="pack">
  <div class="word-pattern" role="img" aria-label="Hand-lettered pattern of the words vegan, raw, organic, non-gmo, gluten-free, kosher, paleo, cruelty-free"></div>

  <svg class="top-band" viewBox="0 0 836 150" aria-hidden="true">
    <polygon fill="var(--flavor-red)" points="0,0 836,0 836,128 826,140 814,128 802,140 790,128 778,140 766,128 754,140 742,128 730,140 718,128 706,140 694,128 682,140 670,128 658,140 646,128 634,140 622,128 610,140 598,128 586,140 574,128 562,140 550,128 538,140 526,128 514,140 502,128 490,140 478,128 466,140 454,128 442,140 430,128 418,140 406,128 394,140 382,128 370,140 358,128 346,140 334,128 322,140 310,128 298,140 286,128 274,140 262,128 250,140 238,128 226,140 214,128 202,140 190,128 178,140 166,128 154,140 142,128 130,140 118,128 106,140 94,128 82,140 70,128 58,140 46,128 34,140 22,128 10,140 0,128"/>
    <rect x="26" y="42" width="784" height="100" fill="none" stroke="#ea5c6b" stroke-width="2"/>
  </svg>

  <div class="window" role="img" aria-label="Clear window showing round cranberry nut cookies"></div>

  <div class="brand">Sunny Grove Bites</div>
  <div class="subtitle">RAW VEGAN ORGANIC</div>
  <div class="product-name line-1">NUT</div>
  <div class="product-name line-2">COOKIES</div>

  <svg class="flavor-banner" viewBox="0 0 576 84" aria-hidden="true">
    <polygon fill="var(--flavor-red-dark)" points="0,20 40,20 40,84 0,84 14,52"/>
    <polygon fill="var(--flavor-red-dark)" points="576,20 536,20 536,84 576,84 562,52"/>
    <rect x="14" y="0" width="548" height="72" fill="var(--flavor-red)"/>
  </svg>
  <div class="flavor-name">Cranberry</div>

  <div class="net-weight">Net Wt: 100 g</div>

  <section class="claims-band">
    <div class="claim"><span class="claim-badge"></span><span class="claim-label">Vegan</span></div>
    <div class="claim"><span class="claim-badge"></span><span class="claim-label">Raw</span></div>
    <div class="claim"><span class="claim-badge"></span><span class="claim-label">Organic</span></div>
    <div class="claim"><span class="claim-badge"></span><span class="claim-label">Non-gmo</span></div>
    <div class="claim"><span class="claim-badge"></span><span class="claim-label">Paleo</span></div>
    <div class="claim"><span class="claim-badge"></span><span class="claim-label">Gluten-free</span></div>
    <div class="claim"><span class="claim-badge"></span><span class="claim-label">kosher</span></div>
    <div class="claim"><span class="claim-badge"></span><span class="claim-label">Cruelty-free</span></div>
  </section>
</main>
</body>
</html>
```